Banner for promote service of debit card

We are PagaVelo and we need the banners to be posted on the facebook and instagram pages.
We want something to communicate that it is an exclusive debit card full of services.
Low commissions.
Our competitors:
https://www.nortapay-pagos.it/it/home.html
https://www.zelkor-conti.it/it/
https://www.fotoreelz.it/serravanbank/
sendquillo
maybe some banner that makes the idea of a convenient debit card that everyone can use.
Girls enjoying card shopping.
Please check also website for slogans and phrases to use
https://www.pagavelo-carta.it/
Should show the services.
We must convey that it is a fast, simple card that guarantees privacy.
We need strong banners that attract people as these ban will be sponsored on instagram and facebook
Target Market(s)
People 18-35 y
Open Bank account. low commissions. Easy to use. No limits. 100% Privacy.
Requirements
Must have
- Written in Italian.

```html
<!DOCTYPE html>
<html lang="it">
<head>
<meta charset="utf-8">
<title>PagaVelo – Una carta per tutti</title>
<link href="https://fonts.googleapis.com/css2?family=Oswald:wght@500;600&family=Open+Sans:wght@400;600&display=swap" rel="stylesheet">
<style>
  :root {
    --page-bg: #f3f2f0;
    --violet-deep: #4a1a6e;
    --violet: #7b2a8e;
    --magenta: #c2306f;
    --plum-dark: #3a1450;
    --sun-yellow: #f5c21b;
    --amber: #e39a16;
    --white: #ffffff;
    --ink: #2a1236;
    --skin-warm: #c98a78;
    --rose: #a8466f;
    --card-dark: #2b2733;
  }
  * { margin: 0; padding: 0; box-sizing: border-box; }
  html, body {
    width: 1200px; height: 800px; overflow: hidden;
    background: var(--page-bg);
  }
  .banner {
    position: absolute; left: 280px; top: 30px;
    width: 640px; height: 740px; overflow: hidden;
    background: linear-gradient(135deg, var(--violet-deep) 0%, var(--violet) 45%, var(--magenta) 100%);
    font-family: "Open Sans", sans-serif;
    color: var(--white);
  }
  .banner__shapes { position: absolute; inset: 0; }
  .banner__photo {
    position: absolute; left: 110px; top: 40px; width: 420px; height: 540px;
    border-radius: 200px 200px 24px 24px;
    background: linear-gradient(180deg, var(--skin-warm) 0%, var(--rose) 55%, rgba(123,42,142,0.35) 100%);
    opacity: 0.85;
  }
  .banner__card {
    position: absolute; left: 450px; top: 60px; width: 150px; height: 92px;
    border-radius: 10px;
    background: linear-gradient(135deg, #3a3542 0%, var(--card-dark) 100%);
    transform: rotate(-22deg);
  }
  .brand {
    position: absolute; left: 40px; top: 60px;
    display: flex; align-items: center; gap: 12px;
  }
  .brand__dot {
    width: 34px; height: 34px; border-radius: 50%;
    background: var(--sun-yellow);
  }
  .brand__name {
    font-family: "Oswald", sans-serif; font-weight: 500;
    font-size: 26px; color: var(--white); letter-spacing: 0.5px;
  }
  .headline {
    position: absolute; left: 66px; top: 400px;
    font-family: "Oswald", sans-serif; font-weight: 600;
    font-size: 36px; line-height: 38px; text-transform: uppercase;
  }
  .body-copy {
    position: absolute; left: 66px; top: 492px;
    font-size: 17px; line-height: 24px;
  }
  .cta {
    position: absolute; left: 66px; top: 620px;
    width: 180px; height: 38px; border-radius: 19px;
    background: var(--sun-yellow); color: var(--ink);
    font-weight: 600; font-size: 15px;
    display: flex; align-items: center; justify-content: center;
  }
</style>
</head>
<body>
  <div class="banner">
    <svg class="banner__shapes" width="640" height="740" viewBox="0 0 640 740" aria-hidden="true">
      <polygon points="0,560 0,740 150,740" fill="var(--sun-yellow)"/>
      <polygon points="0,620 0,740 90,740" fill="var(--amber)"/>
      <polygon points="640,300 640,470 520,600 480,560" fill="var(--sun-yellow)" opacity="0.9"/>
      <polygon points="640,520 640,740 360,740" fill="var(--plum-dark)" opacity="0.85"/>
      <polygon points="420,740 500,650 540,740" fill="var(--sun-yellow)"/>
      <polyline points="500,360 560,310 640,380" fill="none" stroke="var(--white)" stroke-width="2" opacity="0.5"/>
    </svg>
    <div class="banner__photo" role="img" aria-label="Foto di due ragazze sorridenti ed entusiaste che si abbracciano"></div>
    <div class="banner__card" role="img" aria-label="Carta di debito scura inclinata"></div>
    <div class="brand">
      <span class="brand__dot"></span>
      <span class="brand__name">PagaVelo</span>
    </div>
    <h1 class="headline">All in one!<br>Una carta per tutti!</h1>
    <p class="body-copy">Enjoy your card!<br>Fai quello che vuoi.<br>Nessun limite.<br>Nessun controllo</p>
    <div class="cta">Ottieni la tua Carta</div>
  </div>
</body>
</html>
```